Back Pain

Need a flyer similar to the attached draft. This is to be handed out to prospective patients. Note that Sketch Hive has already designed the logo. If you need a copy please contact me

```html
<!DOCTYPE html>
<html lang="en">
<head>
<meta charset="utf-8">
<title>Tech Neck Flyer</title>
<link rel="stylesheet" href="https://fonts.googleapis.com/css2?family=Bebas+Neue&family=Montserrat:ital,wght@0,600;0,700;1,500&display=swap">
<style>
:root{
  --stage:#3e3e3e;
  --ink:#111111;
  --white:#ffffff;
  --blue:#1a75bc;
  --sky:#1aa3e4;
  --navy:#1b3f8f;
  --green:#8cc63f;
  --teal:#1f9a9a;
  --grey:#b5b5b5;
  --band:#e7e7e7;
  --dark:#2e2e2e;
  --dot:#d0103a;
}
*{margin:0;padding:0;box-sizing:border-box}
html,body{width:1200px;height:613px;overflow:hidden;background:var(--stage)}
.flyer{position:absolute;left:395px;top:16px;width:780px;height:1102px;background:var(--white);
  transform:scale(.5263);transform-origin:top left;overflow:hidden;font-family:"Bebas Neue",sans-serif;color:var(--ink)}
.abs{position:absolute}
.header svg{position:absolute;left:0;top:0}
.brand{position:absolute;left:30px;top:28px;width:240px;text-align:center;color:var(--blue)}
.brand-mark{width:70px;height:70px;border:5px solid var(--blue);border-radius:50%;margin:0 auto 8px}
.brand-name{font-size:26px;line-height:1;letter-spacing:.5px}
.brand-sub{font-size:13px;letter-spacing:2px;line-height:1.2}
.title{position:absolute;left:318px;top:22px;font-size:128px;line-height:1;color:var(--white);letter-spacing:1px}
.figure{position:absolute;left:20px;top:200px;width:280px;height:790px;border-radius:120px 120px 40px 40px;
  background:linear-gradient(180deg,#bdbdbd,#a8a8a8);z-index:2}
.pointers{position:absolute;left:0;top:0;z-index:3}
.symptoms{position:absolute;left:298px;top:210px;color:var(--blue);font-size:30px;line-height:1;z-index:3}
.symptoms li{list-style:none;position:absolute;left:0;white-space:nowrap}
.chart-note{position:absolute;left:443px;top:198px;font-size:29px;line-height:.98}
.chart{position:absolute;left:0;top:0}
.axis-label{position:absolute;left:443px;top:495px;font-size:27px}
.pressure-label{position:absolute;left:748px;top:355px;font-size:25px;transform:translate(-50%,-50%) rotate(-90deg);white-space:nowrap}
.usage{position:absolute;left:345px;top:545px;width:435px;height:126px;background:var(--band)}
.usage-text{position:absolute;left:443px;top:553px;line-height:1}
.usage-lead{color:var(--green);font-size:31px}
.usage-hours{color:var(--blue);font-size:52px}
.usage-tail{font-size:32px}
.care{position:absolute;left:0;top:700px;width:780px;height:196px;background:linear-gradient(120deg,#3a3a3a,#262626 60%,#333)}
.care-text{position:absolute;left:333px;top:712px;line-height:1;z-index:3}
.care-title{color:var(--sky);font-size:66px}
.care-sub{color:var(--white);font-size:24px}
.care-how{color:var(--green);font-size:41px;line-height:1}
.doctor{position:absolute;left:20px;top:905px;color:var(--navy);font-size:52px;line-height:1;z-index:3}
.doctor small{font-family:"Montserrat",sans-serif;font-style:italic;font-weight:500;font-size:16px;color:#333;margin-left:8px}
.location{position:absolute;left:0;top:960px;width:600px;height:40px;background:#ededed;z-index:3;padding:6px 0 0 22px;font-size:26px}
.location span{color:var(--green)}
.offer{position:absolute;left:612px;top:905px;width:150px;height:98px;border-radius:16px 16px 0 0;
  background:linear-gradient(180deg,#ffffff,#cfcfcf);border:3px solid #9a9a9a;text-align:center;line-height:.9;z-index:4}
.offer-big{color:var(--navy);font-size:44px;margin-top:8px}
.offer-small{font-size:21px}
.contact svg{position:absolute;left:0;top:0}
.phone{position:absolute;left:92px;top:1012px;color:var(--white);font-size:62px;line-height:1}
.email{position:absolute;left:92px;top:1072px;color:var(--white);font-family:"Montserrat",sans-serif;font-weight:600;font-size:14px}
.book{position:absolute;left:405px;top:1014px;width:360px;text-align:center;color:var(--white);font-family:"Montserrat",sans-serif}
.book-lead{font-weight:700;font-size:18px}
.web{display:flex;align-items:center;justify-content:center;gap:8px;margin-top:6px;height:32px;border-radius:16px;
  background:var(--green);border:2px solid #ffffff;font-weight:700;font-size:18px}
.web-note{font-weight:500;font-size:11px;margin-top:8px}
</style>
</head>
<body>
<main class="flyer">
  <header class="header">
    <svg width="780" height="166" viewBox="0 0 780 166">
      <defs>
        <linearGradient id="headGrad" x1="0" y1="1" x2="1" y2="0">
          <stop offset="0" stop-color="#177f9a"/>
          <stop offset=".5" stop-color="#2f9a74"/>
          <stop offset="1" stop-color="#7fc23c"/>
        </linearGradient>
      </defs>
      <rect width="780" height="166" fill="#1c1c1c"/>
      <polygon points="252,0 780,0 780,166 318,166" fill="url(#headGrad)"/>
    </svg>
    <div class="brand">
      <div class="brand-mark"></div>
      <div class="brand-name">SPINE EASE CLINIC</div>
      <div class="brand-sub">DR SAM PORTER - CHIROPRACTOR</div>
    </div>
    <h1 class="title">TECH NECK</h1>
  </header>

  <section class="usage"></section>
  <section class="care"></section>

  <div class="figure" role="img" aria-label="Grey silhouette of a person walking while looking down at a phone"></div>

  <svg class="pointers" width="780" height="520" viewBox="0 0 780 520">
    <g stroke="#555" stroke-width="1" stroke-dasharray="2 2">
      <line x1="180" y1="223" x2="288" y2="223"/>
      <line x1="197" y1="273" x2="288" y2="263"/>
      <line x1="245" y1="308" x2="288" y2="308"/>
      <line x1="253" y1="370" x2="288" y2="370"/>
      <line x1="253" y1="420" x2="288" y2="412"/>
      <line x1="237" y1="480" x2="288" y2="480"/>
    </g>
    <g fill="var(--dot)">
      <circle cx="180" cy="223" r="8"/><circle cx="197" cy="273" r="8"/>
      <circle cx="245" cy="308" r="8"/><circle cx="253" cy="370" r="8"/>
      <circle cx="253" cy="420" r="8"/><circle cx="153" cy="428" r="8"/>
      <circle cx="237" cy="480" r="8"/>
    </g>
  </svg>

  <ul class="symptoms">
    <li style="top:0">HEADACHES</li>
    <li style="top:40px">NECK PAIN</li>
    <li style="top:80px">SHOULDER<br>PAIN</li>
    <li style="top:145px">BACK PAIN</li>
    <li style="top:188px">ARM &amp;<br>HAND PAIN</li>
    <li style="top:256px">SCIATICA</li>
  </ul>

  <p class="chart-note">AS THE HEAD TILTS FOWARD.<br>MORE FORCE IS PLACED<br>ON THE SPINE</p>
  <svg class="chart" width="780" height="520" viewBox="0 0 780 520" font-family="Bebas Neue, sans-serif">
    <defs>
      <linearGradient id="barGrad" x1="0" y1="0" x2="0" y2="1">
        <stop offset="0" stop-color="#8cc63f"/>
        <stop offset=".55" stop-color="#2ba39a"/>
        <stop offset="1" stop-color="#1a6fbf"/>
      </linearGradient>
    </defs>
    <rect x="445" y="308" width="60" height="78" rx="28" fill="#9a9a9a" role="img" aria-label="Grey head profile icon tilting forward"/>
    <g fill="url(#barGrad)">
      <rect x="445" y="418" width="42" height="37"/>
      <rect x="500" y="360" width="42" height="95"/>
      <rect x="556" y="315" width="42" height="140"/>
      <rect x="612" y="280" width="42" height="175"/>
      <rect x="667" y="243" width="42" height="212"/>
    </g>
    <g fill="#fff" font-size="30" text-anchor="middle">
      <text x="466" y="450">12</text><text x="521" y="420">27</text>
      <text x="577" y="395">40</text><text x="633" y="380">49</text>
      <text x="688" y="350">60</text>
    </g>
    <g fill="#111" font-size="34" text-anchor="middle">
      <text x="466" y="490">0°</text><text x="521" y="490">15°</text>
      <text x="577" y="490">30°</text><text x="633" y="490">45°</text>
      <text x="688" y="490">60°</text>
    </g>
  </svg>
  <p class="axis-label">DEGREES OF FORWARD HEAD TILT</p>
  <p class="pressure-label">PRESSURE ON SPINE (LBS)</p>

  <svg class="abs" style="left:0;top:0;z-index:3" width="780" height="700" viewBox="0 0 780 700">
    <circle cx="350" cy="607" r="76" fill="#1a6fbf"/>
    <path d="M350,607 L350,531 A76,76 0 0 1 395,668 Z" fill="var(--green)"/>
  </svg>
  <div class="usage-text">
    <div class="usage-lead">THE AVERRAGE PERSON SPEND</div>
    <div class="usage-hours">8-11 HOURS PER DAY</div>
    <div class="usage-tail">USING ELECTRONIC DEVICES</div>
  </div>

  <div class="care-text">
    <div class="care-title">CHIROPRACTIC CARE</div>
    <div class="care-sub">CAN HELP CORRECT AND PREVENT THESE PROBLEMS</div>
    <div class="care-how">BY RESTORING AND MAINTAINING<br>PROPER ALIGNMENT OF THE NECK</div>
  </div>

  <div class="doctor">DR. SAMUEL PORTER<small>Chiropractor</small></div>
  <div class="location">NOW IN BAYSIDE @ &nbsp;<span>42 HARBOUR RD - ATRIUM SUITES</span></div>
  <div class="offer">
    <div class="offer-big">50% OFF</div>
    <div class="offer-small">INITIAL<br>CONSULTATION</div>
  </div>

  <footer class="contact">
    <svg width="780" height="1102" viewBox="0 0 780 1102">
      <defs>
        <linearGradient id="webGrad" x1="0" y1="0" x2="1" y2="1">
          <stop offset="0" stop-color="#1d6fb0"/>
          <stop offset="1" stop-color="#102e5c"/>
        </linearGradient>
        <linearGradient id="phoneGrad" x1="0" y1="0" x2="1" y2="0">
          <stop offset="0" stop-color="#6fb52f"/>
          <stop offset="1" stop-color="#9bd243"/>
        </linearGradient>
      </defs>
      <path d="M360,1002 Q420,990 480,1002 T600,1000 T700,1002 T780,996 L780,1102 L360,1102 Z" fill="url(#webGrad)"/>
      <polygon points="0,1000 362,1000 386,1050 362,1102 0,1102" fill="url(#phoneGrad)"/>
      <g fill="none" stroke="#fff" stroke-width="4" stroke-linejoin="round">
        <rect x="40" y="1025" width="30" height="52" rx="5"/>
        <line x1="50" y1="1032" x2="60" y2="1032"/>
        <circle cx="55" cy="1068" r="3" fill="#fff"/>
        <path d="M76,1040 a10,10 0 0 1 0,16 M82,1034 a18,18 0 0 1 0,28"/>
      </g>
    </svg>
    <div class="phone">0400 555 018</div>
    <div class="email">samuel@spineeaseclinic.example</div>
    <div class="book">
      <div class="book-lead">If You Book Online AT</div>
      <div class="web">
        <svg width="18" height="18" viewBox="0 0 18 18" fill="none" stroke="#fff" stroke-width="1.6">
          <circle cx="9" cy="9" r="7.5"/><ellipse cx="9" cy="9" rx="3.3" ry="7.5"/><line x1="1.5" y1="9" x2="16.5" y2="9"/>
        </svg>
        www.spineeaseclinic.example
      </div>
      <div class="web-note">*Choose "Tech Neck" Option</div>
    </div>
  </footer>
</main>
</body>
</html>
```